physio rehab flyer for Vela Mend please

Specification:
Flyer is to be trifold from letter size (8.5 x 11)
-----------------------This may help you:--------------------------
I would like the look of :
clean, minimalistic look with mainly blue and green
san serif font
professional
The colors I like are blue (not the blue in the logo enclosed, I want a change, but more like the blue on my website logo) and light green.
This is my website: www.velamendgroup.ca just so you get an idea but it will be totally changed soon to a to be determined design.
I like the blue and green in file "sample 2" (enclosed)
I like the pictures in "sample 2" file enclosed
For inspiration, I like design of this brochure: http://www.qwelnet.ca/HarbourRehab/PatientsFamilies/Clinics_Tests/DKLT_Service/Documents/Brochure.pdf
Here's how I see the pages layout:
----[location: this should be the cover (outside, right panel of trifold)]-----
Vela Mend Logo
Integrated Injury Rehab
Evidence-based, one-on-one care to make your recovery fast and comfortable
www.velamendgroup.ca
---------------[location: inside, left panel]----------------------------------------
Our team leaders
[portrait here]
Harriet Olsson, MD, FRCPC, MSC, CIME
Physiatrist
Dr. Olsson specializes in injury rehab and sports medicine. She is highly trained having received her MD and Residency in Physiatry from Wexford Crown College. Her passion is to help injured people get back to their life.
[portrait here]
Bronwyn Tessaro, PT
Physiotherapist
Bronwyn has over 10 years of experience as a Physiotherapist (5 in Canada). She has advanced training in orthopedics and manual therapy. She loves and relates well with people from the youngest to the most senior.
--------------------[location: inside, middle panel]-------------------------------
Our services
We provide integrated assessment and care from interprofessional team of regulated healthcare professionals with proven experience in injury rehabilitation:
physiatrists
sport medicine physicians
physiotherapists
chiropractors
massage therapists
acupuncturists
psychologists
We provide custom medical bracing, orthotics, orthopedic shoes, assistive devices, and medical stockings, all in one place.
----------------------[location: inside, right panel]-----------------------------------
Only registered physiotherapists
We strongly believe in consistency with your treatment plan. This means that you spend your time here one-on-one with your physiotherapist, not any students or assistants. You get consistent high quality care from a professional.
One-on-one attention
We book maximum 3 people per hour to ensure everyone gets adequate one-on-one time with their physiotherapist. This compares favorably with other clinics, who may book upwards of 5-6 per hour. The atmosphere is professional -balanced with friendly, caring and relaxed. Our highly qualified staff operate this way to help make your recovery faster and more enjoyable.
------------------------[location: outside, left panel]---------------------------------
The right rehab for your clients
Timely access to comprehensive assessment and treatment
Proven track record in injury rehabilitation
Convenient one-stop service
Customized treatment plans
Integrated, co-ordinated care
Evidence-based care applying leading best practices
Access to specialty clinics: Physiatry and Chronic Pain
-------------------------[location: outside, middle panel]--------------------------
Please call us 416-555-0142
for more information on injury rehabilitation
Vela Mend Group
2819 Barlow Rd., Unit 5
Scarborough, ON M4X 8R2
[Please include a line art map designed based on "map" file enclosed]
To make a referral for your clients, contact velamendgroup@mailbox-example.ca or fax: 416-555-0187. Thank you.
www.velamendgroup.ca
------------------------------------------------------------------------------------------------
Target Market(s)
family doctors, ER docs, lawyers, and general public age (20-50)
Industry/Entity Type
Health And Wellness
Requirements
Must have
- san serif font
- blue and green colors
- clean, sophisticated look
Nice to have
- consumer choice award badge either on front or back of trifold
Should not have
- see above

```html
<!DOCTYPE html>
<html lang="en">
<head>
<meta charset="utf-8">
<title>Vela Mend — Inside Panels</title>
<link href="https://fonts.googleapis.com/css2?family=Open+Sans:ital,wght@0,400;0,600;1,400&display=swap" rel="stylesheet">
<style>
  :root {
    --brand-blue: #4f82c5;
    --heading-blue: #3f74b9;
    --leaf-green: #5a9f3a;
    --ink: #1f1f1f;
    --paper: #ffffff;
    --frame: #ffffff;
  }
  * { margin: 0; padding: 0; box-sizing: border-box; }
  html, body { width: 1200px; height: 927px; overflow: hidden; background: var(--paper); }
  body { font-family: "Open Sans", Arial, sans-serif; color: var(--ink); }
  .brochure { position: relative; width: 1200px; height: 927px; overflow: hidden; background: var(--paper); }

  .panel-team { position: absolute; left: 0; top: 0; width: 400px; height: 927px; background: var(--brand-blue); color: #fff; }
  .panel-heading-light { position: absolute; left: 20px; top: 20px; font-size: 23px; font-weight: 400; }
  .portrait { position: absolute; border: 5px solid var(--frame); }
  .portrait-physiatrist { left: 34px; top: 72px; width: 168px; height: 176px; background: linear-gradient(160deg, #a58b78, #e9e4df 60%, #c9b2a2); }
  .portrait-physio { left: 218px; top: 400px; width: 150px; height: 178px; background: linear-gradient(160deg, #dfe6ea, #c49a86 55%, #b3788a); }
  .leader-name { position: absolute; font-size: 19px; line-height: 1.3; white-space: nowrap; }
  .leader-name .credentials { font-size: 14.5px; }
  .leader-name .role { display: block; font-style: italic; font-size: 19px; margin-top: 4px; }
  .name-physiatrist { left: 210px; top: 168px; }
  .name-physio { left: 14px; top: 526px; }
  .leader-bio { position: absolute; font-size: 15.5px; line-height: 22px; width: 372px; white-space: nowrap; }
  .bio-physiatrist { left: 25px; top: 271px; }
  .bio-physio { left: 14px; top: 602px; }
  .mascot { position: absolute; left: 92px; top: 722px; width: 170px; height: 196px; border-radius: 45% 45% 30% 30%; background: radial-gradient(circle at 50% 40%, #c9a17a, #9c7350 75%); }

  .curves { position: absolute; left: 400px; top: 0; width: 800px; height: 927px; }

  .section-heading { position: absolute; color: var(--heading-blue); font-size: 23px; font-weight: 400; padding-bottom: 6px; border-bottom: 2px solid var(--heading-blue); }
  .heading-services { left: 413px; top: 18px; width: 376px; padding-left: 4px; }
  .heading-registered { left: 810px; top: 18px; width: 380px; padding-left: 3px; }

  .body-copy { position: absolute; font-size: 15px; line-height: 22px; }
  .services-intro { left: 412px; top: 76px; width: 382px; }
  .service-list { position: absolute; left: 513px; top: 175px; list-style: none; font-size: 15px; }
  .service-list li { height: 29.3px; padding-left: 14px; position: relative; }
  .service-list li::before { content: ""; position: absolute; left: 0; top: 8px; width: 6px; height: 6px; border-radius: 50%; background: var(--heading-blue); }
  .registered-copy { left: 818px; top: 77px; width: 370px; font-size: 15.3px; }

  .supplies-copy { left: 412px; top: 825px; width: 380px; color: #fff; }
  .attention-heading { position: absolute; left: 812px; top: 659px; color: #fff; font-size: 22px; font-weight: 400; }
  .attention-copy { left: 814px; top: 699px; width: 380px; color: #fff; font-size: 15.3px; white-space: nowrap; }
</style>
</head>
<body>
<main class="brochure">

  <section class="panel-team">
    <h2 class="panel-heading-light">Our team leaders</h2>
    <div class="portrait portrait-physiatrist" role="img" aria-label="Portrait of Dr. Harriet Olsson, physiatrist, in a white coat with stethoscope"></div>
    <p class="leader-name name-physiatrist">Harriet Olsson,<br><span class="credentials">MD, FRCPC, MSC, CIME</span><span class="role">Physiatrist</span></p>
    <p class="leader-bio bio-physiatrist">Dr. Olsson specializes in injury rehab and sports<br>medicine. She is highly trained having received<br>her MD and Residency in Physiatry from<br>Wexford Crown College. Her passion is to help<br>injured people get back to their life.</p>

    <div class="portrait portrait-physio" role="img" aria-label="Portrait of Bronwyn Tessaro, physiotherapist"></div>
    <p class="leader-name name-physio">Bronwyn Tessaro, PT<span class="role">Physiotherapist</span></p>
    <p class="leader-bio bio-physio">Bronwyn has over 10 years of experience as a<br>Physiotherapist (5 in Canada). She has advanced<br>training in orthopedics and manual therapy. She<br>loves and relates well with people form the<br>youngest to the most senior.</p>

    <div class="mascot" role="img" aria-label="Teddy bear wearing a stethoscope"></div>
  </section>

  <svg class="curves" viewBox="0 0 800 927">
    <defs>
      <linearGradient id="therapy-tones" x1="0" y1="0" x2="1" y2="1">
        <stop offset="0" stop-color="#e7cdbd"/>
        <stop offset="0.45" stop-color="#f1ece8"/>
        <stop offset="0.7" stop-color="#9fc3e3"/>
        <stop offset="1" stop-color="#cfd9e2"/>
      </linearGradient>
    </defs>
    <path role="img" aria-label="Physiotherapist adjusting a hinged knee brace on a patient's leg"
      d="M0,350 C60,388 140,404 260,404 C420,404 560,376 660,386 C720,392 770,430 800,478 C680,505 560,620 440,738 C330,800 150,792 0,762 Z"
      fill="url(#therapy-tones)"/>
    <path d="M0,762 C150,792 330,800 440,738 C560,620 680,505 800,478 L800,927 L0,927 Z" fill="var(--brand-blue)"/>
    <path d="M0,326 C60,372 140,394 260,394 C420,394 560,362 660,372 C720,380 770,420 800,505" fill="none" stroke="var(--leaf-green)" stroke-width="7"/>
  </svg>

  <h2 class="section-heading heading-services">Our services</h2>
  <p class="body-copy services-intro">We provide integrated assessment and care from interprofessional team of regulated healthcare professionals with proven experience in injury rehabilitation:</p>
  <ul class="service-list">
    <li>physiatrists</li>
    <li>sport medicine physicians</li>
    <li>physiotherapists</li>
    <li>chiropractors</li>
    <li>massage therapists</li>
    <li>acupuncturists</li>
    <li>psychologists</li>
  </ul>
  <p class="body-copy supplies-copy">We provide custom medical bracing, orthotics, orthopedic shoes, assistive devices, and medical stockings, all in one place.</p>

  <h2 class="section-heading heading-registered">Only registered physiotherapists</h2>
  <p class="body-copy registered-copy">We strongly believe in consistency with your treatment plan. This means that you spend your time here one-on-one with your physiotherapist, not any students or assistants. You get consistent high quality care from a professional.</p>

  <h2 class="attention-heading">One-on-one attention</h2>
  <p class="body-copy attention-copy">We book maximum 3 people per hour to ensure<br>everyone gets adequate one-on-one time with<br>their physiotherapist.&nbsp; This compares favorably<br>with other clinics, who may book upwards of<br>5-6 per hour. The atmosphere is<br>professional -balanced with friendly, caring and<br>relaxed. Our highly qualified staff operate this<br>way to help make your recovery faster and more<br>enjoyable.</p>

</main>
</body>
</html>
```